WERBE-FLYER
Zielgruppe
Immobilien Makler
Aufgabenstellung
Überarbeitung des bestehenden Entwurfs.
Der Flyer wird an Hauseigentümer mit der Post verteilt (nicht adressierte Werbung).
Format:
offen A4 Querformat
geschlossen (1x gefaltet) A5 (4 Seiten)
In der Mitte eine Perforationslinie zum Abtrennen. Danach kann die Seite 3 & 4 zusammengefaltet (geklebt) werden und an uns zurückgeschickt werden.
Rücksendung erfolgt via Geschäftsantwortsendung - ohne Strichcode (siehe Vorlage Alpin. Kurier).

```html
<!DOCTYPE html>
<html lang="de">
<head>
<meta charset="utf-8">
<title>NOVERA Immobilien – Flyer</title>
<link href="https://fonts.googleapis.com/css2?family=Source+Sans+3:wght@400;600;700&display=swap" rel="stylesheet">
<style>
:root{
  --stage:#939699;
  --paper:#ffffff;
  --navy:#1e3550;
  --teal:#1eb1c8;
  --ink:#2b2b2b;
  --band:#e8e8e9;
}
*{margin:0;padding:0;box-sizing:border-box}
html,body{width:849px;height:1200px;overflow:hidden;background:var(--stage)}
body{position:relative;font-family:"Source Sans 3",sans-serif;color:var(--ink)}
.sheet{position:absolute;left:67px;width:715px;height:505px;background:var(--paper);overflow:hidden}
.sheet--outside{top:72px}
.sheet--inside{top:624px}
.abs{position:absolute}

/* outside */
.reply-mark{left:253px;top:4px;font-size:27px;font-weight:700;color:#111;line-height:1}
.reply-note{left:299px;top:14px;font-size:3.6px;line-height:4.6px;color:#444}
.reply-type{left:243px;top:43px;width:125px;text-align:center;font-size:3.8px;line-height:5px;font-weight:700;color:#222}
.recipient{left:186px;top:102px;font-size:7.6px;line-height:11px}
.brand{left:532px;top:36px;display:flex;align-items:center;gap:6px}
.brand__mark{width:22px;height:22px;background:var(--navy)}
.brand__name{font-size:30px;font-weight:400;color:var(--navy);letter-spacing:1px;line-height:1}
.hero{left:357px;top:101px;width:358px;height:404px;
  background:linear-gradient(180deg,#aab6c6 0%,#c9cdd2 30%,#e3ddd2 55%,#b9a58c 75%,#7b7d6e 100%)}
.claim{left:532px;top:361px;width:156px;height:68px;background:var(--navy);color:#fff;
  padding:5px 0 0 12px;font-size:19.5px;line-height:20.5px;letter-spacing:2.6px}
.claim__accent{color:var(--teal);letter-spacing:10.5px}
.weblink{left:532px;top:480px;width:156px;height:25px;background:var(--navy);color:#fff;
  font-size:10.5px;font-weight:600;letter-spacing:1.6px;text-align:center;line-height:25px}

/* inside */
.edge{width:12px}
.edge--left{left:0}
.edge--right{left:703px}
.edge__accent{top:50px;height:24px;background:var(--teal)}
.edge__base{top:74px;height:431px;background:var(--navy)}
.tape{left:357px;height:24px;background:var(--band);text-align:center;font-size:7.2px;letter-spacing:1.3px;line-height:24px;color:#333}
.tape--top{top:0;width:358px}
.tape--bottom{top:481px;width:346px}
.perforation{left:356px;top:0;height:505px;border-left:1px dashed #8a8a8a}
.scissors{left:349px;top:444px}
.heading{top:52px;font-size:19.5px;color:var(--teal);letter-spacing:.2px;line-height:22px}
.col-left{left:36px;width:300px}
.col-right{left:393px;width:274px}
.subhead{font-size:11.6px;color:var(--navy);line-height:14px}
.copy{font-size:7.6px;line-height:11px}
.bullets{list-style:none;font-size:7.6px;line-height:11px}
.bullets li{position:relative;padding-left:14px}
.bullets li::before{content:"";position:absolute;left:0;top:3px;width:5px;height:5px;background:var(--teal)}
.brand--small{left:36px;top:401px}
.brand--small .brand__mark{width:14px;height:14px}
.brand--small .brand__name{font-size:19px}
.contact{top:443px;font-size:7.6px;line-height:11px}
.quote{top:808px;font-size:10.6px;line-height:13.6px;color:var(--navy)}
.fold-note{top:242px;font-size:5px;font-weight:600;color:var(--navy)}
.fold-line{left:393px;top:252px;width:273px;border-top:1px dashed var(--teal)}
.reply-title{top:257px;font-size:12.8px;font-weight:700;color:var(--teal)}
.prompt{top:280px;font-size:7.6px}
.yes{top:298px;font-size:10px;font-weight:700;color:var(--teal)}
.option{font-size:7.6px;line-height:10px;display:flex;align-items:center;gap:3px}
.option__box{width:8px;height:8px;border:1px solid var(--teal)}
.field{left:393px;width:273px;border-bottom:1px solid var(--teal);font-size:7.6px;line-height:10px;padding-bottom:1px}
</style>
</head>
<body>

<section class="sheet sheet--outside">
  <div class="abs reply-mark">A</div>
  <div class="abs reply-note">Nicht frankieren<br>Ne pas affranchir<br>Non affrancare</div>
  <div class="abs reply-type">Geschäftsantwortsendung&nbsp; Invio commerciale risposta<br>Envoi commercial-réponse</div>

  <address class="abs recipient" style="font-style:normal">NOVERA IMMOBILIEN AG<br>Lindenweg 12<br>8003 Zürich</address>

  <div class="abs brand"><span class="brand__mark"></span><span class="brand__name">NOVERA</span></div>

  <div class="abs hero" role="img" aria-label="Foto: moderner weisser Hauseingang mit Holzsteg und Gartenbepflanzung in der Abenddämmerung"></div>
  <div class="abs claim">IMMOBILIEN<br>SIND UNSERE<br><span class="claim__accent">PASSION</span></div>
  <div class="abs weblink">www.novera-immo.ch</div>
</section>

<section class="sheet sheet--inside">
  <div class="abs edge edge--left edge__accent"></div>
  <div class="abs edge edge--left edge__base"></div>
  <div class="abs edge edge--right edge__accent"></div>
  <div class="abs edge edge--right edge__base"></div>

  <div class="abs tape tape--top">KLEBESTREIFEN</div>
  <div class="abs tape tape--bottom">KLEBESTREIFEN</div>
  <div class="abs perforation"></div>
  <svg class="abs scissors" width="14" height="20" viewBox="0 0 14 20" aria-hidden="true">
    <g fill="none" stroke="#1eb1c8" stroke-width="1.2">
      <line x1="3" y1="1" x2="9" y2="13"/><line x1="11" y1="1" x2="5" y2="13"/>
      <circle cx="4.3" cy="16" r="2.6"/><circle cx="9.7" cy="16" r="2.6"/>
    </g>
  </svg>

  <!-- services -->
  <h2 class="abs heading col-left" style="font-weight:400">UNSERE DIENSTLEISTUNGEN</h2>
  <h3 class="abs subhead col-left" style="top:93px;font-weight:400">Verkauf mit Passion und Sachverstand</h3>
  <p class="abs copy col-left" style="top:112px;width:300px">Der Verkauf einer Immobilie ist ein vielschichtiger Prozess. Lieb gewonnene Liegenschaften, die über viele Jahre ein Zuhause waren, haben für die Verkäufer nicht nur einen Geldwert, sondern auch einen emotionalen Wert. Wir begleiten unsere Kunden mit Passion und Sachverstand durch jede Phase des Verkaufsprozesses.</p>
  <ul class="abs bullets col-left" style="top:168px">
    <li>Erstes Gespräch und Besichtigung der Immobilie</li>
    <li>Ermitteln des bestmöglichen Verkaufspreises</li>
    <li>Erstellen von Verkaufsunterlagen und Vermarktung des Objekts</li>
    <li>Qualifizierern der Kaufinteressenten</li>
    <li>Finanzierungsberatung für Kaufinteressenten</li>
    <li>Preisverhandlungen und ausarbeiten des Kaufvertrags</li>
    <li>Begleitung bei der Beurkundung und Eigentumsübertragung</li>
  </ul>
  <h3 class="abs subhead col-left" style="top:263px;font-weight:400">Schätzung des Immobilienwerts</h3>
  <p class="abs copy col-left" style="top:282px;width:300px">Damit unsere Kunden den bestmöglichen Preisfür ihr Haus, ihre Eigentums-<br>wohnung oder ihr Grundstück erzielen, ermitteln wir den genauen Wert.<br>Unsere Schätzung ergibt eine übersichtliche Aufstellung zum Gebäude,<br>der Lage, dem wirtschaftlichen Wert und Angaben zum Verkehrswert der<br>Immobilie. Wir wenden je nach Objekt die folgenden Bewertungsmethoden an:</p>
  <ul class="abs bullets col-left" style="top:337px">
    <li>Sachwert-, Ertragswert-oder Mischwertmethode</li>
    <li>Hedonische Bewertungen, Residualwertverfahren<br>oder DCF (Discounted-Cash-Flow-Verfahren)</li>
  </ul>

  <div class="abs brand brand--small"><span class="brand__mark"></span><span class="brand__name">NOVERA</span></div>
  <address class="abs contact" style="left:36px;font-style:normal">NOVERA IMMOBILIEN AG<br>Lindenweg 12<br>8003 Zürich</address>
  <div class="abs contact" style="left:143px">Tel. 044 000 12 30<br>Fax 044 000 12 35</div>
  <div class="abs contact" style="left:232px">info@novera-immo.ch<br>www.novera-immo.ch</div>

  <!-- values & reply -->
  <h2 class="abs heading col-right" style="font-weight:400;width:300px">UNSERE WERTE UND VISIONEN</h2>
  <p class="abs copy col-right" style="top:112px;width:290px">Jede Immobilie ist so einzigartig, wie die Menschen, denen sie gehört. Für uns zählt der Mensch, die Liegenschaft und die gemeinsame Geschichte. In über 20 Jahren haben wir das Immobiliengeschäft und all seine Facetten verinnerlicht. Das macht uns zu einem kompetenten und engagierten Partner für alle Fragen rund um Immobilien.</p>
  <p class="abs subhead col-right" style="top:185px;font-size:10.6px;line-height:13.6px">Immobilien sind unsere Passion<br>und die Zufriedenheit<br>der Kunden ist unser Ziel.</p>

  <div class="abs fold-note col-right">Bitte 1x falten und an den Klebestreifen zusammenkleben</div>
  <div class="abs fold-line"></div>
  <h3 class="abs reply-title col-right">Rückantwort</h3>
  <p class="abs prompt col-right">Bitte kreuzen Sie Ihre Wünsche an:</p>
  <div class="abs yes col-right">Ja,</div>
  <div class="abs option col-right" style="top:316px"><span class="option__box"></span>... wir denken über einen Verkauf unserer Immobilie nach</div>
  <div class="abs option col-right" style="top:334px"><span class="option__box"></span>... wir sind am Kauf einer Wohnung/Haus interessiert</div>
  <div class="abs option col-right" style="top:352px"><span class="option__box"></span>... wir wünschen ein unverbindliches persönliches Gespräch</div>

  <div class="abs field" style="top:374px">Name/Vorname</div>
  <div class="abs field" style="top:396px">Strasse Nr.</div>
  <div class="abs field" style="top:418px">PLZ /Ort</div>
  <div class="abs field" style="top:440px">Telefon</div>
  <div class="abs field" style="top:462px">E-Mail</div>
</section>

</body>
</html>
```